Diabetes control iOS/Android app design

I need a modern app design with light colors that are easy on the eyes, This app is for diabetes control. Focusing on Sweet/carb control and its daily intake .. I have uploaded some wireframe pages to design . Light colors are preferred for design. I donot need too much Hussle and data on main page.
Name/title: Glypath- Diabetes restore

Target Market(s)

Diabetes patients

Industry/Entity Type

health

Colors
0094D4
00A9DD
6FCCEA
C7EBF8
E9F6FB
00AB8E
00BBA5
67D7C9
C6EFE9
E9F9F6
59FF00
82FF00
B8FF75
E3FFCB
F4FFEA
FFC000
F8CF3A
FAE287
FDF2CF
FEFAEE

Requirements
Should not have
• complicated design. It should be simple , modern and easy o eye.

```html
<!DOCTYPE html>
<html lang="en">
<head>
<meta charset="utf-8">
<title>Sugar Control Reversal – App Screens</title>
<link href="https://fonts.googleapis.com/css2?family=Poppins:wght@400;500;600;700&display=swap" rel="stylesheet">
<style>
:root{
  --teal:#1ba085;
  --teal-light:#67d7c9;
  --yellow:#f8bb3a;
  --yellow-soft:#fcc94a;
  --ink:#222;
  --body-top:#fffcf5;
  --body-bottom:#fde1ab;
  --canvas:#d0d0d0;
  --white:#fff;
  --blue:#0094d4;
}
*{margin:0;padding:0;box-sizing:border-box}
html,body{width:1200px;height:834px;overflow:hidden;background:var(--canvas);font-family:'Poppins',sans-serif;color:var(--ink)}
.screen{position:absolute;top:95px;width:375px;height:812px;transform:scale(.7926);transform-origin:0 0;border-radius:26px;overflow:hidden;background:linear-gradient(var(--body-top),var(--body-bottom))}
.screen--home{left:82px}.screen--monitor{left:452px}.screen--plan{left:821px}
.header-bg{position:absolute;left:0;top:0}
.status-time{position:absolute;left:22px;top:19px;color:var(--white);font-size:15px;font-weight:500}
.status-icons{position:absolute;right:20px;top:22px}
.round-btn{position:absolute;top:71px;width:35px;height:35px;border-radius:50%;display:flex;align-items:center;justify-content:center}
.round-btn--back{left:22px;background:var(--white)}
.round-btn--menu{right:22px;background:var(--yellow-soft)}
.app-title{position:absolute;left:0;right:0;top:65px;text-align:center;color:var(--white);font-weight:600;font-size:18px;line-height:25px;letter-spacing:-.2px}
.center{position:absolute;left:0;right:0;text-align:center}
.section-title{font-weight:600;font-size:20px;letter-spacing:-.3px}
.underline{position:absolute;left:164px;width:47px;height:2px;background:var(--yellow)}
.count-card{position:absolute;left:22px;top:261px;width:331px;height:55px;border:1.5px solid var(--teal);border-radius:28px;background:var(--white);display:flex;align-items:center;padding:0 18px 0 9px}
.count-badge{width:38px;height:38px;border-radius:50%;background:var(--teal);color:var(--white);font-weight:600;font-size:16px;display:flex;align-items:center;justify-content:center}
.count-label{margin-left:17px;font-size:17px;font-weight:500;flex:1}
.count-value{color:var(--yellow);font-weight:600;font-size:16px}
.gauge-label{position:absolute;font-size:13px;font-weight:500}
.chart-card{position:absolute;left:23px;width:330px;background:var(--white);border:1.5px solid var(--teal);border-radius:16px;overflow:hidden}
.check-list{position:absolute;left:22px;top:666px;list-style:none}
.check-list li{display:flex;align-items:center;gap:17px;font-size:17px;font-weight:500;height:33px}
.avatar{position:absolute;left:151px;top:233px;width:74px;height:74px;border-radius:50%;background:linear-gradient(#fafafa,#e6e6e6);border:2px solid #fff;box-shadow:0 2px 6px rgba(0,0,0,.08);display:flex;align-items:center;justify-content:center;font-size:38px;font-weight:700;color:#aaa}
.plan-button{position:absolute;left:22px;top:334px;width:332px;height:56px;border:2px solid var(--yellow-soft);border-radius:28px;background:var(--white);display:flex;align-items:center;justify-content:center;gap:8px;color:var(--teal);font-weight:600;font-size:16px}
.plan-heading{top:422px;font-weight:600;font-size:20px;line-height:29px;letter-spacing:-.3px}
.plan-intro{top:525px;color:var(--teal);font-weight:500;font-size:18.5px;line-height:28px}
.plan-steps{top:594px;font-size:16px;font-weight:500;line-height:31px}
.plan-steps p:last-child{line-height:24px;margin-top:4px}
.nav-bar{position:absolute;left:22px;top:746px;width:332px;height:52px;border-radius:26px;background:var(--teal);display:flex;justify-content:space-around;align-items:center;padding:0 4px}
.nav-item{width:34px;height:34px;border-radius:50%;border:1.5px solid var(--white);display:flex;align-items:center;justify-content:center}
.nav-item--active{background:var(--yellow-soft);border-color:var(--yellow-soft)}
</style>
</head>
<body>

<!-- Screen 1: Home -->
<section class="screen screen--home">
  <svg class="header-bg" width="375" height="160"><path d="M0 0H375V95Q188 215 0 95Z" fill="var(--teal)"/></svg>
  <div class="status-time">9:41</div>
  <svg class="status-icons" width="70" height="12" viewBox="0 0 70 12"><g fill="#fff"><rect x="0" y="9" width="2" height="3"/><rect x="4" y="6" width="2" height="6"/><rect x="8" y="3" width="2" height="9"/><rect x="12" y="0" width="2" height="12"/><path d="M30 11l-2.5-3a4 4 0 0 1 5 0zM24.5 5a8.5 8.5 0 0 1 11 0l-1.5 1.6a6.3 6.3 0 0 0-8 0zM22 2.4a12 12 0 0 1 16 0l-1.4 1.6a10 10 0 0 0-13.2 0z"/><rect x="47" y="1.5" width="19" height="9" rx="2" fill="none" stroke="#fff"/><rect x="49" y="3.5" width="15" height="5" rx="1"/><rect x="67" y="4.5" width="1.5" height="3"/></g></svg>
  <div class="round-btn round-btn--back"><svg width="14" height="10"><path d="M5 1L1 5l4 4M1 5h12" stroke="var(--blue)" stroke-width="2" fill="none"/></svg></div>
  <div class="app-title">SUGAR CONTROL<br>REVERSAL</div>
  <div class="round-btn round-btn--menu"><svg width="12" height="10"><path d="M0 1h12M0 5h12M0 9h12" stroke="#fff" stroke-width="1.6"/></svg></div>

  <div class="center section-title" style="top:204px">SUGAR COUNT</div>
  <div class="underline" style="top:232px"></div>
  <div class="count-card"><span class="count-badge">01</span><span class="count-label">Sugar Today</span><span class="count-value">62%</span></div>

  <div class="center section-title" style="top:366px">CONSUMPTION TODAY</div>
  <div class="underline" style="top:394px"></div>
  <div class="center" style="top:427px;font-size:13px;font-weight:500">Fatal / 3</div>
  <svg style="position:absolute;left:0;top:440px" width="375" height="140" viewBox="0 0 375 140">
    <g transform="translate(188 120)" stroke="none">
      <path d="M-108 0A108 108 0 0 1 -87.4 -63.5L-44.5 -32.3A55 55 0 0 0 -55 0Z" fill="#f23a12"/>
      <path d="M-87.4 -63.5A108 108 0 0 1 -33.4 -102.7L-17 -52.3A55 55 0 0 0 -44.5 -32.3Z" fill="#fb7d10"/>
      <path d="M-33.4 -102.7A108 108 0 0 1 33.4 -102.7L17 -52.3A55 55 0 0 0 -17 -52.3Z" fill="#fcd115"/>
      <path d="M33.4 -102.7A108 108 0 0 1 87.4 -63.5L44.5 -32.3A55 55 0 0 0 17 -52.3Z" fill="#8ccd08"/>
      <path d="M87.4 -63.5A108 108 0 0 1 108 0L55 0A55 55 0 0 0 44.5 -32.3Z" fill="#0fbc0f"/>
      <path d="M-6 6L-11 -4L48 -66Z" fill="#7c7c7c"/>
      <circle cx="-6" cy="0" r="9" fill="#7c7c7c"/>
      <circle cx="-6" cy="0" r="2.5" fill="#fff"/>
    </g>
  </svg>
  <div class="gauge-label" style="left:56px;top:565px">Danger / 1</div>
  <div class="gauge-label" style="left:251px;top:565px">Catastrophe / 5</div>

  <nav class="nav-bar">
    <span class="nav-item nav-item--active"><svg width="16" height="14"><path d="M8 0L0 7h2v7h4.5V9.5h3V14H14V7h2z" fill="#fff"/></svg></span>
    <span class="nav-item"><svg width="16" height="14"><path d="M1 0v13h15M3 10l4-4 3 2 5-6" stroke="#fff" stroke-width="1.6" fill="none"/></svg></span>
    <span class="nav-item"><svg width="16" height="16"><rect x="1" y="2" width="12" height="12" rx="2" stroke="#fff" stroke-width="1.6" fill="none"/><path d="M4 8l3 3 8-9" stroke="#fff" stroke-width="1.6" fill="none"/></svg></span>
    <span class="nav-item"><svg width="14" height="15"><circle cx="7" cy="4" r="3.6" fill="#fff"/><path d="M0 15a7 6 0 0 1 14 0z" fill="#fff"/></svg></span>
    <span class="nav-item"><svg width="16" height="16" viewBox="-8 -8 16 16"><circle r="5.5" stroke="#fff" stroke-width="4" stroke-dasharray="2.2 2.1" fill="none"/><circle r="4.6" fill="#fff"/><circle r="1.8" fill="var(--teal)"/></svg></span>
  </nav>
</section>

<!-- Screen 2: Rehab monitor -->
<section class="screen screen--monitor">
  <svg class="header-bg" width="375" height="160"><path d="M0 0H375V95Q188 215 0 95Z" fill="var(--teal)"/></svg>
  <div class="status-time">9:41</div>
  <svg class="status-icons" width="70" height="12" viewBox="0 0 70 12"><g fill="#fff"><rect x="0" y="9" width="2" height="3"/><rect x="4" y="6" width="2" height="6"/><rect x="8" y="3" width="2" height="9"/><rect x="12" y="0" width="2" height="12"/><path d="M30 11l-2.5-3a4 4 0 0 1 5 0zM24.5 5a8.5 8.5 0 0 1 11 0l-1.5 1.6a6.3 6.3 0 0 0-8 0zM22 2.4a12 12 0 0 1 16 0l-1.4 1.6a10 10 0 0 0-13.2 0z"/><rect x="47" y="1.5" width="19" height="9" rx="2" fill="none" stroke="#fff"/><rect x="49" y="3.5" width="15" height="5" rx="1"/><rect x="67" y="4.5" width="1.5" height="3"/></g></svg>
  <div class="round-btn round-btn--back"><svg width="14" height="10"><path d="M5 1L1 5l4 4M1 5h12" stroke="var(--blue)" stroke-width="2" fill="none"/></svg></div>
  <div class="app-title">SUGAR CONTROL<br>REVERSAL</div>
  <div class="round-btn round-btn--menu"><svg width="12" height="10"><path d="M0 1h12M0 5h12M0 9h12" stroke="#fff" stroke-width="1.6"/></svg></div>

  <div class="center section-title" style="top:180px;font-size:18.5px">REHAB MONITOR</div>
  <div class="underline" style="top:208px"></div>

  <div class="chart-card" style="top:230px;height:171px">
    <svg width="330" height="171" viewBox="23 230 330 171" font-family="Poppins, sans-serif">
      <text x="188" y="253" text-anchor="middle" font-size="13" font-weight="500" fill="#222">Daily Sugar Graph</text>
      <g stroke="#eee" stroke-width=".7">
        <path d="M58 256H332M58 273H332M58 291H332M58 308H332M58 326H332M58 343H332M58 361H332"/>
      </g>
      <g font-size="5.5" fill="#555" text-anchor="end">
        <text x="54" y="258">700</text><text x="54" y="275">600</text><text x="54" y="293">500</text><text x="54" y="310">400</text><text x="54" y="328">300</text><text x="54" y="345">200</text><text x="54" y="363">100</text>
      </g>
      <path d="M83 337L118 278L147 266L169 310L223 280L279 309L316 301V377H83Z" fill="#6fe4d3" opacity=".85"/>
      <path d="M83 337L118 278L147 266L169 310L223 280L279 309L316 301" stroke="#1fd0b0" stroke-width="1.3" fill="none"/>
      <path d="M83 361L106 344L132 319L168 353L210 331L254 337L316 353V377H83Z" fill="#9aa99b" opacity=".55"/>
      <path d="M83 361L106 344L132 319L168 353L210 331L254 337L316 353" stroke="#d9344a" stroke-width="1.2" fill="none"/>
      <path d="M83 345L114 361L168 340L261 369L316 366" stroke="#f5b82a" stroke-width="1.2" fill="none"/>
      <g fill="#fff" stroke-width="1.2">
        <g stroke="#1fd0b0"><circle cx="83" cy="337" r="2.4"/><circle cx="118" cy="278" r="2.4"/><circle cx="147" cy="266" r="2.4"/><circle cx="169" cy="310" r="2.4"/><circle cx="223" cy="280" r="2.4"/><circle cx="279" cy="309" r="2.4"/><circle cx="316" cy="301" r="2.4"/></g>
        <g stroke="#d9344a"><circle cx="83" cy="361" r="2.4"/><circle cx="106" cy="344" r="2.4"/><circle cx="132" cy="319" r="2.4"/><circle cx="168" cy="353" r="2.4"/><circle cx="210" cy="331" r="2.4"/><circle cx="254" cy="337" r="2.4"/><circle cx="316" cy="353" r="2.4"/></g>
        <g stroke="#f5b82a"><circle cx="83" cy="345" r="2.4"/><circle cx="114" cy="361" r="2.4"/><circle cx="168" cy="340" r="2.4"/><circle cx="261" cy="369" r="2.4"/><circle cx="316" cy="366" r="2.4"/></g>
      </g>
      <rect x="124" y="303" width="16" height="8" rx="1.5" fill="#d9344a"/><text x="132" y="309" font-size="5.5" fill="#fff" text-anchor="middle">372</text>
      <rect x="160" y="324" width="16" height="8" rx="1.5" fill="#f5b82a"/><text x="168" y="330" font-size="5.5" fill="#fff" text-anchor="middle">260</text>
      <rect x="307" y="284" width="17" height="8" rx="1.5" fill="#1fd0b0"/><text x="315.5" y="290" font-size="5.5" fill="#fff" text-anchor="middle">405</text>
      <path d="M58 254V377H332" stroke="#222" stroke-width="1.2" fill="none"/>
    </svg>
  </div>

  <div class="center section-title" style="top:422px;font-size:18.5px">DAILY WALK/EXERCISE</div>
  <div class="underline" style="top:450px"></div>

  <div class="chart-card" style="top:473px;height:170px">
    <svg width="330" height="170" viewBox="23 473 330 170" font-family="Poppins, sans-serif">
      <g stroke="#ececec" stroke-width=".7">
        <path d="M62 489H330M62 511H330M62 533H330M62 555H330M62 577H330M62 599H330"/>
        <path d="M88 485V620M126 485V620M164 485V620M202 485V620M240 485V620M278 485V620M316 485V620"/>
      </g>
      <g font-size="5.5" fill="#444" text-anchor="end">
        <text x="56" y="491">120</text><text x="56" y="513">100</text><text x="56" y="535">80</text><text x="56" y="557">60</text><text x="56" y="579">40</text><text x="56" y="601">20</text><text x="56" y="622">0</text>
      </g>
      <path d="M62 620H330" stroke="#999" stroke-width=".8"/>
      <g fill="var(--teal)">
        <rect x="71" y="511" width="7" height="109"/><rect x="109" y="522" width="7" height="98"/><rect x="148" y="565" width="7" height="55"/><rect x="186" y="511" width="7" height="109"/><rect x="223" y="511" width="7" height="109"/><rect x="261" y="555" width="7" height="65"/><rect x="299" y="565" width="7" height="55"/>
      </g>
      <g fill="#fdbf4b">
        <rect x="83" y="522" width="7" height="98"/><rect x="121" y="533" width="7" height="87"/><rect x="160" y="511" width="7" height="109"/><rect x="198" y="555" width="7" height="65"/><rect x="235" y="522" width="7" height="98"/><rect x="273" y="538" width="7" height="82"/><rect x="311" y="511" width="7" height="109"/>
      </g>
      <g font-size="4.5" fill="#222" text-anchor="middle">
        <text x="74.5" y="508">100</text><text x="86.5" y="519">90</text><text x="112.5" y="519">90</text><text x="124.5" y="530">80</text><text x="151.5" y="562">50</text><text x="163.5" y="508">100</text><text x="189.5" y="508">100</text><text x="201.5" y="552">60</text><text x="226.5" y="508">100</text><text x="238.5" y="519">90</text><text x="264.5" y="552">60</text><text x="276.5" y="535">75</text><text x="302.5" y="562">50</text><text x="314.5" y="508">100</text>
        <text x="80" y="628">Sun</text><text x="118" y="628">Mon</text><text x="157" y="628">Tue</text><text x="195" y="628">Wed</text><text x="232" y="628">Thu</text><text x="270" y="628">Fri</text><text x="308" y="628">Sat</text>
      </g>
    </svg>
  </div>

  <ul class="check-list">
    <li><svg width="18" height="18"><circle cx="9" cy="9" r="8.5" fill="var(--teal)"/><path d="M5 9.2l2.8 2.8 5-5.5" stroke="#fff" stroke-width="2" fill="none"/></svg>Sugar Bite Sent Weekly</li>
    <li><svg width="18" height="18"><circle cx="9" cy="9" r="8.5" fill="var(--teal)"/><path d="M5 9.2l2.8 2.8 5-5.5" stroke="#fff" stroke-width="2" fill="none"/></svg>Weekly Average</li>
  </ul>

  <nav class="nav-bar">
    <span class="nav-item"><svg width="16" height="14"><path d="M8 0L0 7h2v7h4.5V9.5h3V14H14V7h2z" fill="#fff"/></svg></span>
    <span class="nav-item nav-item--active"><svg width="16" height="14"><path d="M1 0v13h15M3 10l4-4 3 2 5-6" stroke="#fff" stroke-width="1.6" fill="none"/></svg></span>
    <span class="nav-item"><svg width="16" height="16"><rect x="1" y="2" width="12" height="12" rx="2" stroke="#fff" stroke-width="1.6" fill="none"/><path d="M4 8l3 3 8-9" stroke="#fff" stroke-width="1.6" fill="none"/></svg></span>
    <span class="nav-item"><svg width="14" height="15"><circle cx="7" cy="4" r="3.6" fill="#fff"/><path d="M0 15a7 6 0 0 1 14 0z" fill="#fff"/></svg></span>
    <span class="nav-item"><svg width="16" height="16" viewBox="-8 -8 16 16"><circle r="5.5" stroke="#fff" stroke-width="4" stroke-dasharray="2.2 2.1" fill="none"/><circle r="4.6" fill="#fff"/><circle r="1.8" fill="var(--teal)"/></svg></span>
  </nav>
</section>

<!-- Screen 3: Rehab plan -->
<section class="screen screen--plan">
  <svg class="header-bg" width="375" height="160"><path d="M0 0H375V95Q188 215 0 95Z" fill="var(--teal)"/></svg>
  <div class="status-time">9:41</div>
  <svg class="status-icons" width="70" height="12" viewBox="0 0 70 12"><g fill="#fff"><rect x="0" y="9" width="2" height="3"/><rect x="4" y="6" width="2" height="6"/><rect x="8" y="3" width="2" height="9"/><rect x="12" y="0" width="2" height="12"/><path d="M30 11l-2.5-3a4 4 0 0 1 5 0zM24.5 5a8.5 8.5 0 0 1 11 0l-1.5 1.6a6.3 6.3 0 0 0-8 0zM22 2.4a12 12 0 0 1 16 0l-1.4 1.6a10 10 0 0 0-13.2 0z"/><rect x="47" y="1.5" width="19" height="9" rx="2" fill="none" stroke="#fff"/><rect x="49" y="3.5" width="15" height="5" rx="1"/><rect x="67" y="4.5" width="1.5" height="3"/></g></svg>
  <div class="round-btn round-btn--back"><svg width="14" height="10"><path d="M5 1L1 5l4 4M1 5h12" stroke="var(--blue)" stroke-width="2" fill="none"/></svg></div>
  <div class="app-title">SUGAR CONTROL<br>REVERSAL</div>
  <div class="round-btn round-btn--menu"><svg width="12" height="10"><path d="M0 1h12M0 5h12M0 9h12" stroke="#fff" stroke-width="1.6"/></svg></div>

  <div class="center section-title" style="top:180px">REHAB PLAN</div>
  <div class="underline" style="top:208px"></div>
  <div class="avatar">R</div>
  <div class="plan-button">REHAB PLAN <svg width="15" height="15"><circle cx="7.5" cy="7.5" r="7" fill="var(--teal)"/><path d="M4 7.5h6M7.5 4.5l3 3-3 3" stroke="#fff" stroke-width="1.8" fill="none"/></svg></div>

  <div class="center plan-heading">SEE YOUR PLAN TO ACHIEVE<br>NO MEDICINE DIABETES<br>CONTROL</div>
  <div class="underline" style="top:509px"></div>
  <div class="center plan-intro">Create your plan in just a<br>few steps:</div>
  <div class="center plan-steps">
    <p>Choose desired date</p>
    <p>Follow suggested diet</p>
    <p>Enter your readings (Sugar,<br>Frequency, Diet)</p>
  </div>

  <nav class="nav-bar">
    <span class="nav-item"><svg width="16" height="14"><path d="M8 0L0 7h2v7h4.5V9.5h3V14H14V7h2z" fill="#fff"/></svg></span>
    <span class="nav-item"><svg width="16" height="14"><path d="M1 0v13h15M3 10l4-4 3 2 5-6" stroke="#fff" stroke-width="1.6" fill="none"/></svg></span>
    <span class="nav-item nav-item--active"><svg width="16" height="16"><rect x="1" y="2" width="12" height="12" rx="2" stroke="#fff" stroke-width="1.6" fill="none"/><path d="M4 8l3 3 8-9" stroke="#fff" stroke-width="1.6" fill="none"/></svg></span>
    <span class="nav-item"><svg width="14" height="15"><circle cx="7" cy="4" r="3.6" fill="#fff"/><path d="M0 15a7 6 0 0 1 14 0z" fill="#fff"/></svg></span>
    <span class="nav-item"><svg width="16" height="16" viewBox="-8 -8 16 16"><circle r="5.5" stroke="#fff" stroke-width="4" stroke-dasharray="2.2 2.1" fill="none"/><circle r="4.6" fill="#fff"/><circle r="1.8" fill="var(--teal)"/></svg></span>
  </nav>
</section>

</body>
</html>
```